We want to revamp our current website -www.tolvex-eng.com

We need to have a new website for our company that offers non-destructive and testing solutions around Africa. We have a current website but it does not fulfil our needs as it is:<br/>1. Not clear and bright<br/>2. Does not fit well in mobile <br/>3. Is not easily updatable by our staff. <br/>4. Is not linked to our social media sites.<br/>We would like to have a website that addresses the above issues. Our colours are Red and Blue and should communicate to our clients, that we are a professional company open for business, ready to solve their non-destructive testing problems around Africa. * Helpful if it is a wordpress website.

Target Market(s)

Our customers are B2B Corporate clients. We mainly work in
1. Storage Terminals
2. Refineries
3. Oil and Gas offshore and onshore rigs.

Industry/Entity Type

Oil And Gas

Contact Information for Business Card

Please find our current business card on the uploaded files.

Coding

Coded - Design and coding required

Number of Pages Required

5+ page

Font styles to use
Serif
Sans Serif

Requirements
Must have
• I like this site www.pirelt-inspection.com They are in the same industry.
• I don't understand how to call them but all the 'call to action' buttons, and links to our Social media pages.
• Must have a place where we update information in a regular basis. A Blog!

```html
<!DOCTYPE html>
<html lang="en">
<head>
<meta charset="utf-8">
<title>Tolvex Engineering</title>
<link rel="stylesheet" href="https://fonts.googleapis.com/css2?family=Anton&family=Poppins:wght@300;400;500;600&family=Roboto:wght@400&display=swap">
<style>
:root{
  --red:#a50f15;
  --blue:#223063;
  --navy:#1c2a5a;
  --ink:#333;
  --muted:#666;
  --soft:#f3f3f6;
  --white:#fff;
}
*{margin:0;padding:0;box-sizing:border-box}
html,body{width:1200px;height:3245px;overflow:hidden}
body{position:relative;font-family:"Poppins",sans-serif;color:var(--ink);background:var(--white)}
.abs{position:absolute}
.topbar{left:0;top:0;width:1200px;height:42px;background:var(--red)}
.topbar .call{position:absolute;right:80px;top:0;height:42px;display:flex;align-items:center;gap:10px;color:var(--white);font-size:15px;font-weight:600}
.topbar .call .ico{width:30px;height:30px;border-radius:50%;background:var(--blue);display:flex;align-items:center;justify-content:center}
.header{left:0;top:42px;width:1200px;height:82px;background:var(--white);box-shadow:0 1px 3px rgba(0,0,0,.08)}
.brand{position:absolute;left:76px;top:6px;width:150px;height:120px;border-radius:50%;background:var(--white);box-shadow:0 2px 6px rgba(0,0,0,.15);display:flex;align-items:center;justify-content:center;z-index:3}
.brand span{font-weight:600;font-size:28px;color:var(--blue)}
.nav{position:absolute;left:296px;right:82px;top:0;height:82px;display:flex;justify-content:space-between;align-items:center;list-style:none;font-size:14.5px;color:#333}
.nav li{position:relative;height:82px;display:flex;align-items:center}
.nav li.active{color:var(--red)}
.nav li.active::after{content:"";position:absolute;left:-6px;right:-6px;bottom:0;height:4px;background:var(--red)}
.hero{left:0;top:124px;width:1200px;height:630px;background:radial-gradient(ellipse at 45% 40%,#4a4a36 0%,#2b2a22 45%,#16160f 100%)}
.hero-title{left:0;top:285px;width:1200px;text-align:center;font-family:"Anton",sans-serif;font-size:66px;color:var(--white);letter-spacing:.5px}
.hero-sub{left:0;top:372px;width:1200px;text-align:center;font-family:"Roboto",sans-serif;font-size:23px;color:var(--white)}
.btn{display:flex;align-items:center;justify-content:center;background:var(--red);color:var(--white);border-radius:30px;font-weight:500;font-size:18px;text-transform:uppercase}
.arrow-btn{width:46px;height:46px;border-radius:50%;background:rgba(34,48,99,.8);display:flex;align-items:center;justify-content:center}
.eyebrow{color:var(--red);font-size:21px}
.h2{color:var(--blue);font-weight:500;font-size:40px}
.svc{background:var(--white);border-radius:12px;box-shadow:0 2px 10px rgba(0,0,0,.12)}
.svc .pic{position:absolute;left:9px;top:9px;right:9px;height:208px}
.svc .name{position:absolute;left:0;right:0;bottom:22px;text-align:center;font-size:20px;font-weight:500;color:#333}
.about p{font-size:14.5px;line-height:27px;color:#555;width:420px;margin-bottom:9px}
.cta{left:0;top:1857px;width:1200px;height:249px;background:var(--blue)}
.post{background:var(--white);box-shadow:0 2px 10px rgba(0,0,0,.1)}
.post .pic{position:absolute;left:0;top:0;width:100%;height:214px;border-radius:0 0 50% 50%/0 0 38% 38%}
.post .date{position:absolute;left:0;right:0;top:253px;text-align:center;color:var(--red);font-size:17px;font-weight:500}
.post h3{position:absolute;left:0;right:0;top:287px;text-align:center;color:var(--blue);font-size:17.5px;font-weight:500;line-height:25px}
.post .more{position:absolute;left:50%;top:356px;transform:translateX(-50%)}
.footer{left:0;top:2763px;width:1200px;height:482px;background:linear-gradient(180deg,#1e2b5d 0%,#253266 50%,#1b2754 100%)}
.flogo{left:524px;top:2700px;width:152px;height:132px;border-radius:50%;background:var(--white);display:flex;align-items:center;justify-content:center;box-shadow:0 2px 8px rgba(0,0,0,.2)}
.flogo span{font-weight:600;font-size:28px;color:var(--blue)}
.social{width:60px;height:60px;border-radius:50%;background:var(--blue);border:3px solid #c9ccd6}
.contact-ico{width:90px;height:90px;border-radius:50%;background:var(--red);border:4px solid var(--white);display:flex;align-items:center;justify-content:center}
.contact-txt{width:260px;text-align:center;color:#dfe2ec;font-size:15px;line-height:25px;font-weight:300}
.copy{left:0;top:3201px;width:1200px;text-align:center;color:var(--white);font-size:14px}
.copy b{color:var(--red);font-weight:400}
</style>
</head>
<body>

<div class="abs topbar">
  <div class="call">Call Us On :
    <span class="ico"><svg width="16" height="16" viewBox="0 0 24 24"><path d="M6.6 10.8a15 15 0 0 0 6.6 6.6l2.2-2.2c.3-.3.7-.4 1-.2 1.1.4 2.3.6 3.6.6.6 0 1 .4 1 1V20c0 .6-.4 1-1 1A17 17 0 0 1 3 4c0-.6.4-1 1-1h3.5c.6 0 1 .4 1 1 0 1.3.2 2.5.6 3.6.1.3 0 .7-.2 1z" fill="#fff"/></svg></span>
    + 254 20 418 0392/3</div>
</div>

<div class="abs header">
  <div class="brand"><span>Tolvex</span></div>
  <ul class="nav">
    <li class="active">Home</li><li>About Us</li><li>Inspection</li><li>NDT Services</li><li>Advance NDT Services</li><li>Engineering Services</li><li>Contact Us</li>
  </ul>
</div>

<div class="abs hero" role="img" aria-label="Close-up of a technician holding an ultrasonic flaw detector"></div>
<svg class="abs" style="left:0;top:540px" width="1200" height="220" viewBox="0 540 1200 220">
  <path d="M0,760 L0,635 C20,650 40,712 85,716 C125,718 120,640 165,612 C205,590 235,640 255,665 C290,700 300,600 320,575 C345,545 410,540 425,585 C440,640 470,690 520,705 C590,720 640,700 655,665 C670,630 700,600 745,632 C790,665 820,735 880,740 C960,748 1000,690 1015,640 C1035,585 1080,570 1120,575 C1160,580 1185,600 1200,612 L1200,760 Z" fill="#fff"/>
  <circle cx="286" cy="636" r="42" fill="#223063"/>
  <circle cx="856" cy="699" r="30" fill="#223063"/>
</svg>
<div class="abs hero-title">Tolvex Engineering</div>
<div class="abs hero-sub">We offer inspection &amp; engineering services</div>
<div class="abs btn" style="left:511px;top:423px;width:177px;height:51px">Contact Us</div>
<div class="abs arrow-btn" style="left:14px;top:357px"><svg width="14" height="22" viewBox="0 0 14 22"><path d="M11 2 2 11l9 9" stroke="#fff" stroke-width="2" fill="none"/></svg></div>
<div class="abs arrow-btn" style="left:1139px;top:357px"><svg width="14" height="22" viewBox="0 0 14 22"><path d="m3 2 9 9-9 9" stroke="#fff" stroke-width="2" fill="none"/></svg></div>

<div class="abs eyebrow" style="left:0;top:786px;width:1200px;text-align:center">What We Do</div>
<div class="abs h2" style="left:0;top:820px;width:1200px;text-align:center">Services We Provide</div>

<svg class="abs" style="left:0;top:1160px" width="1200" height="700" viewBox="0 1160 1200 700">
  <path d="M0,1390 C300,1400 500,1385 650,1322 C800,1258 1000,1250 1200,1355 L1200,1860 L0,1860 Z" fill="#f3f3f6"/>
  <circle cx="0" cy="1290" r="120" fill="#a50f15"/>
  <circle cx="185" cy="1394" r="42" fill="#a50f15"/>
</svg>

<div class="abs svc" style="left:183px;top:913px;width:258px;height:292px">
  <div class="pic" role="img" aria-label="Engineer working on wellhead valves" style="background:linear-gradient(180deg,#5d6066,#8a8a82 60%,#55574f)"></div>
  <div class="name">Engineering Services</div>
</div>
<div class="abs svc" style="left:472px;top:910px;width:261px;height:292px">
  <div class="pic" role="img" aria-label="Inspector testing a rail track" style="background:linear-gradient(180deg,#4d5055,#7b7670 55%,#5a5752)"></div>
  <div class="name">NDT Services</div>
</div>
<div class="abs svc" style="left:762px;top:908px;width:259px;height:292px">
  <div class="pic" role="img" aria-label="Ultrasonic testing device in use" style="background:linear-gradient(180deg,#3a3226,#8a6a2e 50%,#5a8a85)"></div>
  <div class="name">Advance NDT Services</div>
</div>

<div class="abs" role="img" aria-label="Line drawing of an articulated robotic inspection arm" style="left:176px;top:1404px;width:410px;height:453px;background:linear-gradient(135deg,#e9e9ee,#dcdce3)"></div>

<div class="abs about" style="left:648px;top:1434px">
  <div class="eyebrow">Welcome To</div>
  <div class="h2" style="margin-top:2px;margin-bottom:18px">Tolvex-eng</div>
  <p>Our operations are split into two divisions, Tolvex Inspection Services and Tolvex Engineering services.</p>
  <p>We pick the best talent from the industry and have heavily invested in our developing our staff skills further through regular rigorous external and internal training to keep up with the industry trends.</p>
</div>
<div class="abs btn" style="left:646px;top:1735px;width:166px;height:50px;font-size:16px">Learn More</div>

<div class="abs cta">
  <div class="abs" style="left:0;top:50px;width:1200px;text-align:center;color:#fff;font-size:30px;font-weight:500;line-height:40px">If you have an any Question for<br>Contact Us Today !</div>
  <div class="abs btn" style="left:511px;top:148px;width:177px;height:50px">Contact Us</div>
</div>

<div class="abs" style="left:0;top:2165px;width:1200px;text-align:center;color:var(--blue);font-size:42px;font-weight:600">BLOG POST</div>

<div class="abs post" style="left:101px;top:2256px;width:311px;height:403px">
  <div class="pic" role="img" aria-label="Refinery construction site with pipelines" style="background:linear-gradient(180deg,#6f8db5,#a9b3bb 55%,#4d5358)"></div>
  <div class="date">18 - Feb -2020</div>
  <h3>Lorem Ipsum is Simply dummy<br>Text of the Printing</h3>
  <svg class="more" width="28" height="12" viewBox="0 0 28 12"><path d="M0 6h25M20 1l5 5-5 5" stroke="#bbb" stroke-width="2" fill="none"/></svg>
</div>
<div class="abs post" style="left:443px;top:2256px;width:312px;height:403px">
  <div class="pic" role="img" aria-label="Technician inspecting a turbine" style="background:linear-gradient(135deg,#3d3a36,#6b5a48 50%,#8a9a5a)"></div>
  <div class="date">18 - Feb -2020</div>
  <h3>Lorem Ipsum is Simply dummy<br>Text of the Printing</h3>
  <svg class="more" width="28" height="12" viewBox="0 0 28 12"><path d="M0 6h25M20 1l5 5-5 5" stroke="#bbb" stroke-width="2" fill="none"/></svg>
</div>
<div class="abs post" style="left:787px;top:2256px;width:312px;height:403px">
  <div class="pic" role="img" aria-label="Wellhead equipment against a dusky sky" style="background:linear-gradient(180deg,#6a7486,#9aa0a8 55%,#4a4c50)"></div>
  <div class="date">18 - Feb -2020</div>
  <h3>Lorem Ipsum is Simply dummy<br>Text of the Printing</h3>
  <svg class="more" width="28" height="12" viewBox="0 0 28 12"><path d="M0 6h25M20 1l5 5-5 5" stroke="#bbb" stroke-width="2" fill="none"/></svg>
</div>

<div class="abs footer"></div>
<div class="abs flogo"><span>Tolvex</span></div>
<div class="abs social" style="left:534px;top:2866px" role="link" aria-label="Social profile one"></div>
<div class="abs social" style="left:605px;top:2866px" role="link" aria-label="Social profile two"></div>

<svg class="abs" style="left:0;top:3005px" width="1200" height="10"><path d="M400 5H555M645 5H810" stroke="#c9ccd6" stroke-width="2" stroke-dasharray="2 4"/></svg>
<div class="abs contact-ico" style="left:309px;top:2967px"><svg width="40" height="30" viewBox="0 0 40 30"><rect x="2" y="2" width="36" height="26" fill="none" stroke="#fff" stroke-width="2"/><path d="M2 2l18 15L38 2M2 28l13-13M38 28 25 15" fill="none" stroke="#fff" stroke-width="2"/></svg></div>
<div class="abs contact-ico" style="left:555px;top:2967px"><svg width="30" height="40" viewBox="0 0 30 40"><path d="M15 38C15 38 3 22 3 14a12 12 0 0 1 24 0c0 8-12 24-12 24z" fill="none" stroke="#fff" stroke-width="2"/><circle cx="15" cy="14" r="5" fill="none" stroke="#fff" stroke-width="2"/></svg></div>
<div class="abs contact-ico" style="left:811px;top:2967px"><svg width="36" height="36" viewBox="0 0 24 24"><path d="M6.6 10.8a15 15 0 0 0 6.6 6.6l2.2-2.2c.3-.3.7-.4 1-.2 1.1.4 2.3.6 3.6.6.6 0 1 .4 1 1V20c0 .6-.4 1-1 1A17 17 0 0 1 3 4c0-.6.4-1 1-1h3.5c.6 0 1 .4 1 1 0 1.3.2 2.5.6 3.6.1.3 0 .7-.2 1z" fill="none" stroke="#fff" stroke-width="1.3"/></svg></div>
<div class="abs contact-txt" style="left:222px;top:3064px">Email<br>info@tolvex-eng.com</div>
<div class="abs contact-txt" style="left:470px;top:3064px">Kizingo, Harbour Lane<br>P.O. BOX 41820-80100<br>Mombasa Kenya</div>
<div class="abs contact-txt" style="left:721px;top:3064px">Phone<br>+ 254 20 418 0392/3</div>
<div class="abs" style="left:76px;top:3179px;width:1048px;height:1px;background:rgba(255,255,255,.2)"></div>
<div class="abs copy">©<b>Tolvex-eng</b> -2020 All rights reserved.</div>

</body>
</html>
```